Corvana Wound Care Business card design

We need a business card designed around our logo which was provided. The logo of preference is the colored. Also the colors and fonts were provided.

Target Market(s)

Our Referral partners are home health agencies.

Industry/Entity Type

Healthcare

Contact Information for Business Card

Name , Phone #, Email , Title

Requirements
Nice to have
• Creativity
Should not have
• basic

```html
<!DOCTYPE html>
<html lang="en">
<head>
<meta charset="utf-8">
<title>Corvana Wound Care – Business Card</title>
<link rel="stylesheet" href="https://fonts.googleapis.com/css2?family=Lora:wght@400;500&family=Montserrat:wght@500&display=swap">
<style>
  :root {
    --backdrop: #b9bcc1;
    --card-blue: #2b5aa6;
    --card-white: #eef1f6;
    --ink-blue: #244f96;
  }
  * { margin: 0; padding: 0; box-sizing: border-box; }
  html, body {
    width: 1200px; height: 1000px; overflow: hidden;
    background: var(--backdrop);
  }
  .card {
    position: absolute; left: 75px; top: 200px;
    width: 1050px; height: 600px;
    background: var(--card-blue);
    color: var(--card-white);
    font-family: "Lora", Georgia, serif;
    box-shadow: 0 14px 34px rgba(0,0,0,0.22);
    overflow: hidden;
  }
  .brand {
    position: absolute; left: 70px; top: 58px;
    display: flex; align-items: center; gap: 22px;
  }
  .brand-mark {
    width: 58px; height: 58px; background: var(--card-white);
  }
  .brand-name {
    font-size: 50px; font-weight: 500; line-height: 1;
    color: var(--card-white);
  }
  .person { position: absolute; left: 70px; top: 178px; }
  .person-name { font-size: 50px; font-weight: 500; line-height: 1.1; }
  .person-title { font-size: 30px; font-weight: 400; margin-top: 4px; }
  .divider {
    position: absolute; left: 60px; top: 290px;
    width: 440px; height: 2px; background: var(--card-white);
  }
  .contacts {
    position: absolute; left: 78px; top: 318px;
    list-style: none; font-size: 24px; line-height: 1;
  }
  .contacts li { display: flex; align-items: center; gap: 26px; height: 38px; }
  .contacts svg { width: 24px; height: 24px; fill: none; stroke: var(--card-white); stroke-width: 1.8; }
  .web-band {
    position: absolute; left: 0; top: 470px;
    width: 735px; height: 74px; background: var(--card-white);
    display: flex; align-items: center; padding-left: 60px;
    font-family: "Montserrat", Arial, sans-serif; font-weight: 500;
    font-size: 22px; letter-spacing: 7px; color: var(--ink-blue);
  }
  .band-square {
    position: absolute; left: 770px; top: 470px;
    width: 74px; height: 74px; background: var(--card-white);
  }
  .band-tail {
    position: absolute; left: 880px; top: 470px;
    width: 170px; height: 74px; background: var(--card-white);
  }
  .service-area {
    position: absolute; right: 40px; top: 370px;
    text-align: right; font-size: 22px; line-height: 1.45;
  }
</style>
</head>
<body>
  <section class="card" aria-label="Corvana Wound Care business card">
    <div class="brand">
      <span class="brand-mark"></span>
      <span class="brand-name">Corvana Wound Care</span>
    </div>

    <div class="person">
      <h1 class="person-name">Lorem Ipsum</h1>
      <p class="person-title">Managing Director</p>
    </div>
    <div class="divider"></div>

    <ul class="contacts">
      <li>
        <svg viewBox="0 0 24 24"><path d="M5 3h4l2 5-2.5 1.5a11 11 0 0 0 6 6L16 13l5 2v4a2 2 0 0 1-2 2A17 17 0 0 1 3 5a2 2 0 0 1 2-2z"/></svg>
        <span>555-014-2870</span>
      </li>
      <li>
        <svg viewBox="0 0 24 24"><rect x="6" y="3" width="12" height="6"/><rect x="3" y="9" width="18" height="9" rx="2"/><rect x="7" y="14" width="10" height="7"/></svg>
        <span>555-014-3391</span>
      </li>
      <li>
        <svg viewBox="0 0 24 24"><rect x="3" y="5" width="18" height="14"/><path d="M3 5l9 8 9-8"/></svg>
        <span>info@corvanawound.com</span>
      </li>
    </ul>

    <p class="service-area">Harlow, Benton, Marsh<br>&amp; Carver Counties, GA</p>

    <div class="web-band">www.corvanawound.com</div>
    <div class="band-square"></div>
    <div class="band-tail"></div>
  </section>
</body>
</html>
```